Tallow Drifter Business cards

Looking for business card design I already have Logo and some graphics

The website is www.tallowdrifter.example

on the card
First Name Last Name
Title
Website
Phone
Email

```html
<!DOCTYPE html>
<html lang="en">
<head>
<meta charset="utf-8">
<title>Tallow Drifter – Business Cards</title>
<link href="https://fonts.googleapis.com/css2?family=Roboto:wght@400;500;700;900&display=swap" rel="stylesheet">
<style>
  :root {
    --backdrop: #efc13a;
    --card: #ffffff;
    --purple-light: #c866bd;
    --purple-deep: #8a2f84;
    --violet: #5a2a8f;
    --gold: #f2b31c;
    --ink: #25212a;
    --name-purple: #7b2a78;
    --leaf-a: #f2b31c;
    --leaf-b: #7a3a9a;
  }
  * { box-sizing: border-box; margin: 0; padding: 0; }
  html, body { width: 1200px; height: 900px; overflow: hidden; }
  body {
    background: var(--backdrop);
    font-family: "Roboto", Arial, sans-serif;
    position: relative;
  }
  .card {
    position: absolute;
    top: 152px;
    width: 340px;
    height: 595px;
    background: var(--card);
    overflow: hidden;
  }
  .card--front { left: 220px; }
  .card--back { left: 640px; }
  .card__waves { position: absolute; inset: 0; width: 100%; height: 100%; }

  .brand {
    position: absolute;
    left: 0; right: 0;
    display: flex;
    align-items: center;
    justify-content: center;
    gap: 10px;
    font-weight: 900;
    font-size: 30px;
    letter-spacing: 1px;
    text-transform: uppercase;
    color: var(--ink);
  }
  .brand__dot {
    width: 22px; height: 22px;
    border-radius: 50%;
    background: var(--gold);
  }
  .card--front .brand { top: 96px; }
  .card--back .brand { top: 110px; }

  .leaf {
    position: absolute;
    border-radius: 50%;
    background: radial-gradient(circle at 40% 40%, var(--leaf-a) 0%, var(--leaf-a) 35%, var(--leaf-b) 100%);
    opacity: 0.85;
  }

  .contact {
    position: absolute;
    left: 0; right: 0;
    top: 318px;
    text-align: center;
    color: var(--ink);
  }
  .contact__name {
    font-size: 23px;
    font-weight: 500;
    letter-spacing: 1.5px;
    text-transform: uppercase;
  }
  .contact__first { color: var(--name-purple); }
  .contact__title {
    display: inline-block;
    margin-top: 6px;
    padding: 0 14px 6px;
    font-size: 15px;
    border-bottom: 2px solid var(--name-purple);
  }
  .contact__group {
    margin-top: 20px;
    font-size: 13px;
    line-height: 17px;
  }

  .wordmark {
    position: absolute;
    left: 0; right: 0;
    top: 368px;
    text-align: center;
    font-weight: 700;
    font-size: 32px;
    line-height: 42px;
    text-transform: uppercase;
  }
  .wordmark__top { color: var(--name-purple); display: block; }
  .wordmark__bottom { color: var(--gold); display: block; }
</style>
</head>
<body>

  <section class="card card--front" aria-label="Business card front">
    <svg class="card__waves" viewBox="0 0 340 595" aria-hidden="true">
      <defs>
        <linearGradient id="frontPurple" x1="0" y1="0" x2="1" y2="1">
          <stop offset="0" stop-color="#c866bd"/>
          <stop offset="1" stop-color="#8a2f84"/>
        </linearGradient>
      </defs>
      <path d="M0 0 H340 V215 C250 250 120 280 0 300 Z" fill="#f2b31c"/>
      <path d="M0 0 H340 V250 C250 255 140 220 0 190 Z" fill="url(#frontPurple)"/>
      <path d="M110 232 C200 255 280 262 340 250 V282 C270 300 180 280 110 232 Z" fill="#5a2a8f"/>
      <path d="M180 258 C240 272 300 272 340 262 V270 C290 285 230 282 180 258 Z" fill="#1d1822"/>
    </svg>
    <div class="brand"><span class="brand__dot"></span>Tallow Drifter</div>
    <div class="leaf" role="img" aria-label="Leaf illustration" style="left:22px;top:258px;width:64px;height:64px;"></div>
    <div class="leaf" role="img" aria-label="Leaf illustration" style="left:262px;top:300px;width:56px;height:56px;"></div>
    <div class="leaf" role="img" aria-label="Leaf illustration" style="left:14px;top:478px;width:74px;height:74px;"></div>
    <div class="contact">
      <div class="contact__name"><span class="contact__first">Mara</span> Ellison</div>
      <div class="contact__title">Manager</div>
      <div class="contact__group">+00 1234 5678<br>+00 1234 5678</div>
      <div class="contact__group" style="margin-top:10px;">hello@tallowdrifter.example<br>www.tallowdrifter.example</div>
      <div class="contact__group" style="margin-top:10px;">24 Mill Lane<br>Westbury, England</div>
    </div>
  </section>

  <section class="card card--back" aria-label="Business card back">
    <svg class="card__waves" viewBox="0 0 340 595" aria-hidden="true">
      <defs>
        <linearGradient id="backPurple" x1="0" y1="0" x2="1" y2="1">
          <stop offset="0" stop-color="#c866bd"/>
          <stop offset="1" stop-color="#8a2f84"/>
        </linearGradient>
      </defs>
      <path d="M0 0 H340 V230 C250 265 120 280 0 290 Z" fill="#f2b31c"/>
      <path d="M0 0 H340 V268 C250 265 140 235 0 180 Z" fill="url(#backPurple)"/>
      <path d="M100 238 C200 268 280 275 340 268 V298 C270 312 180 292 100 238 Z" fill="#5a2a8f"/>
      <path d="M170 268 C240 285 300 285 340 278 V286 C290 298 230 296 170 268 Z" fill="#1d1822"/>
    </svg>
    <div class="brand"><span class="brand__dot"></span>Tallow Drifter</div>
    <div class="leaf" role="img" aria-label="Leaf illustration" style="left:6px;top:285px;width:62px;height:62px;"></div>
    <div class="leaf" role="img" aria-label="Leaf illustration" style="left:6px;top:500px;width:66px;height:66px;"></div>
    <div class="leaf" role="img" aria-label="Large leaf illustration" style="left:225px;top:460px;width:105px;height:105px;"></div>
    <div class="wordmark">
      <span class="wordmark__top">Tallow</span>
      <span class="wordmark__bottom">Drifter</span>
    </div>
  </section>

</body>
</html>
```